Project Manager Business Card for Top Architectural Firm

Update and design a stunning Senior Project Manager Business Card

MARCO T. DRUMMOND II
Senior Project Manager

H A L C Y O N
A R C H I T E C T U R E L L C.
www.HalcyonGrandEstates.example
4127 NW 52nd Ter. Suite 2308
Miami, FL 33148
C: (305) 555-0184
mdrummond.halcyongrandestates@mailbox.example

Looking to have the logo to be UV Spot ink printed and to be prominent.

Target Market(s)

High end real estate architecture construction

Industry/Entity Type

Architect

Contact Information for Business Card

MARCO T. DRUMMOND II
Senior Project Manager

H A L C Y O N
Miami, FL 33148
C: (305) 555-0184

Font styles to use
Sans Serif

Colors

Designer to choose colors to be used in the design.

Requirements
Must have
• Prominent Logo

```html
<!DOCTYPE html>
<html lang="en">
<head>
<meta charset="utf-8">
<title>Halcyon Architecture – Business Card</title>
<link href="https://fonts.googleapis.com/css2?family=Montserrat:wght@300;500;600;700&display=swap" rel="stylesheet">
<style>
  :root {
    --backdrop: #4a4c50;
    --card: #121214;
    --card-edge: #1c1c1f;
    --accent-blue: #2f86c6;
    --accent-blue-light: #5bb0e4;
    --accent-orange: #e8743a;
    --ink-white: #f2f2f2;
  }
  * { margin: 0; padding: 0; box-sizing: border-box; }
  html, body {
    width: 1200px; height: 1000px; overflow: hidden;
    background: var(--backdrop);
    font-family: "Montserrat", sans-serif;
  }
  .canvas {
    width: 1200px; height: 1000px;
    display: flex; align-items: center; justify-content: center;
  }
  .business-card {
    position: relative;
    width: 1000px; height: 570px;
    border-radius: 40px;
    background: radial-gradient(ellipse at 40% 40%, var(--card-edge), var(--card) 70%);
    overflow: hidden;
    box-shadow: 0 20px 50px rgba(0,0,0,.45);
  }
  .contact-block { position: absolute; left: 72px; top: 118px; }
  .person-name {
    color: var(--accent-blue);
    font-weight: 700; font-size: 34px; letter-spacing: .5px;
  }
  .person-title {
    color: var(--ink-white);
    font-weight: 600; font-size: 24px; margin-top: 6px;
  }
  .contact-list { list-style: none; margin-top: 48px; }
  .contact-item {
    display: flex; align-items: center; gap: 14px;
    color: var(--accent-blue);
    font-weight: 500; font-size: 20px;
    height: 50px;
  }
  .contact-icon { width: 24px; height: 24px; flex: none; }
  .address {
    margin-top: 44px;
    color: var(--accent-blue);
    font-weight: 700; font-size: 23px; line-height: 1.4;
  }
  .brand-block {
    position: absolute; right: 70px; top: 58px;
    display: flex; flex-direction: column; align-items: flex-end;
  }
  .brand-dot {
    width: 120px; height: 120px; border-radius: 50%;
    background: var(--accent-blue-light);
    margin-right: 170px; margin-bottom: 14px;
  }
  .brand-name, .brand-sub {
    color: var(--ink-white);
    font-weight: 300;
  }
  .brand-name { font-size: 66px; letter-spacing: 10px; line-height: 1; }
  .brand-sub { font-size: 20px; letter-spacing: 4px; margin-top: 10px; }
  .accent-rule {
    position: absolute; left: 0; right: 0; height: 3px;
  }
  .accent-rule--orange {
    bottom: 40px;
    background: linear-gradient(90deg, var(--accent-orange), rgba(232,116,58,.25));
  }
  .accent-rule--blue {
    bottom: 35px;
    background: linear-gradient(90deg, var(--accent-blue), rgba(47,134,198,.25));
  }
</style>
</head>
<body>
<main class="canvas">
  <article class="business-card">
    <section class="contact-block">
      <h1 class="person-name">MARCO T. DRUMMOND II</h1>
      <p class="person-title">Senior Project Manager</p>
      <ul class="contact-list">
        <li class="contact-item">
          <svg class="contact-icon" viewBox="0 0 24 24" aria-hidden="true">
            <rect width="24" height="24" rx="5" fill="var(--accent-blue)"/>
            <path d="M8 5.5l2.5 3-1.5 1.8c.8 1.8 2.2 3.2 4 4l1.8-1.5 3 2.5-1.6 2.4C11 17.5 6.5 13 6 7.1z" fill="#fff"/>
          </svg>
          (305) 555-0184
        </li>
        <li class="contact-item">
          <svg class="contact-icon" viewBox="0 0 24 24" aria-hidden="true">
            <rect width="24" height="24" rx="5" fill="var(--accent-blue)"/>
            <circle cx="12" cy="12" r="6.5" fill="none" stroke="#fff" stroke-width="1.5"/>
            <ellipse cx="12" cy="12" rx="2.8" ry="6.5" fill="none" stroke="#fff" stroke-width="1.3"/>
            <line x1="5.5" y1="12" x2="18.5" y2="12" stroke="#fff" stroke-width="1.3"/>
          </svg>
          www.HalcyonGrandEstates.example
        </li>
        <li class="contact-item">
          <svg class="contact-icon" viewBox="0 0 24 24" aria-hidden="true">
            <rect width="24" height="24" rx="5" fill="var(--accent-blue)"/>
            <rect x="5" y="7" width="14" height="10" rx="1" fill="#fff"/>
            <path d="M5.5 7.5l6.5 5 6.5-5" fill="none" stroke="var(--accent-blue)" stroke-width="1.4"/>
          </svg>
          mdrummond.halcyongrandestates@mailbox.example
        </li>
      </ul>
      <address class="address">
        4127 NW 52nd Ter. Suite 2308<br>
        Miami, FL 33148
      </address>
    </section>

    <section class="brand-block">
      <span class="brand-dot" aria-hidden="true"></span>
      <p class="brand-name">HALCYON</p>
      <p class="brand-sub">ARCHITECTURE LLC.</p>
    </section>

    <span class="accent-rule accent-rule--orange"></span>
    <span class="accent-rule accent-rule--blue"></span>
  </article>
</main>
</body>
</html>
```